Design for Certificate for Educational Program

Dear Designer,
We need a design for a certificate once participants graduate from our educational program. You find our website here (pls take the logo from the page):
https://www.tallorium.com/
The briefing for the design should fulfill the following requirements / entail the following elements:
- Name of participant
- Name of program:
Quillnode developer
or
Quillnode architect
- there needs to be a a place on the certificate where a cool hologram would go
- Logo
Research what else should go there / what would be on a certificate.
Style:
- futuristic
- bold
- The program is for software developers - think about what things in this industry look like, what might fit to this target group
- cool
- NOT like a Bachelor program
- colors: blues and greens, maybe some black / grey
- professional
- authority
Our company presentations use Nunito as font. But you can use any font you want as long as it fulfills above requirements.
Timeline is: first delivery by Friday, Dec. 16, 06:00pm ET (Fernwick), the latest.
For questions, pls feel free to approach me.
All the best,
Dr. Morten Haslvik
Software programmers

```html
<!DOCTYPE html>
<html lang="en">
<head>
<meta charset="utf-8">
<title>Quillnode Certificate of Graduation</title>
<link rel="stylesheet" href="https://fonts.googleapis.com/css2?family=Nunito:ital,wght@0,400;0,600;0,800;1,400&family=Orbitron:wght@700&display=swap">
<style>
  :root {
    --bg-deep: #07121d;
    --bg-mid: #0d2233;
    --frame-cyan: #27b6e6;
    --frame-dim: #1d5f7e;
    --brand-cyan: #33b8ea;
    --badge-green: #2fd39a;
    --title-green: #3fe0a4;
    --fill-cyan: #5fd0ff;
    --label-grey: #b9c7d3;
    --leader-grey: #4c6b80;
    --holo-a: #2fd39a;
    --holo-b: #27b6e6;
    --holo-c: #1a3f8f;
  }
  * { margin: 0; padding: 0; box-sizing: border-box; }
  html, body { width: 1200px; height: 894px; overflow: hidden; background: var(--bg-deep); }
  .certificate {
    position: relative; width: 1200px; height: 894px;
    background: radial-gradient(ellipse at 50% 40%, var(--bg-mid) 0%, var(--bg-deep) 75%);
  }
  .frame { position: absolute; inset: 0; }

  .brand-name {
    position: absolute; left: 0; width: 1200px; top: 96px; text-align: center;
    font-family: "Nunito", sans-serif; font-weight: 800; font-size: 88px;
    color: var(--brand-cyan); letter-spacing: 2px; line-height: 1;
  }
  .brand-square {
    position: absolute; left: 549px; top: 217px; width: 106px; height: 101px;
    background: var(--badge-green);
  }
  .title {
    position: absolute; left: 0; width: 1200px; top: 350px; text-align: center;
    font-family: "Orbitron", sans-serif; font-weight: 700; font-size: 44px;
    color: var(--title-green); letter-spacing: 2px; line-height: 1;
  }
  .label {
    position: absolute; font-family: "Nunito", sans-serif; font-style: italic;
    font-size: 20px; color: var(--label-grey); line-height: 1; white-space: nowrap;
  }
  .leader { position: absolute; border-bottom: 2px dotted var(--leader-grey); height: 0; }
  .fill-in {
    position: absolute; font-family: "Nunito", sans-serif; font-weight: 600; font-size: 32px;
    color: var(--fill-cyan); line-height: 1; white-space: nowrap;
  }
  .hologram { position: absolute; left: 495px; top: 573px; width: 250px; height: 250px; }
  .meta-label {
    position: absolute; font-family: "Nunito", sans-serif; font-size: 24px;
    color: var(--label-grey); line-height: 1;
  }
</style>
</head>
<body>
<main class="certificate">
  <svg class="frame" width="1200" height="894" viewBox="0 0 1200 894" aria-hidden="true">
    <rect x="28" y="28" width="1144" height="838" fill="none" stroke="var(--frame-dim)" stroke-width="1.5"/>
    <rect x="40" y="40" width="1120" height="814" fill="none" stroke="var(--frame-cyan)" stroke-width="2"/>
    <g fill="none" stroke="var(--badge-green)" stroke-width="5">
      <path d="M22 92 V22 H92"/>
      <path d="M1108 22 H1178 V92"/>
      <path d="M22 802 V872 H92"/>
      <path d="M1108 872 H1178 V802"/>
    </g>
  </svg>

  <div class="brand-name">Quillnode</div>
  <div class="brand-square"></div>

  <h1 class="title">Certificate of Graduation</h1>

  <span class="label" style="left:90px; top:462px;">This is to certify that Mr. / Mrs.</span>
  <span class="leader" style="left:440px; top:478px; width:465px;"></span>
  <span class="fill-in" style="left:505px; top:438px;">Name of the candidate</span>
  <span class="label" style="left:914px; top:462px;">has completed a course</span>

  <span class="label" style="left:90px; top:531px;">of Graduation in</span>
  <span class="leader" style="left:255px; top:547px; width:474px;"></span>
  <span class="fill-in" style="left:340px; top:506px;">Quillnode developer</span>
  <span class="label" style="left:738px; top:531px;">on</span>
  <span class="leader" style="left:765px; top:547px; width:375px;"></span>
  <span class="fill-in" style="left:872px; top:506px;">01-11-2023</span>

  <svg class="hologram" viewBox="0 0 250 250" role="img" aria-label="Hologram seal area">
    <defs>
      <linearGradient id="holo-fill" x1="0" y1="0" x2="1" y2="1">
        <stop offset="0" stop-color="var(--holo-a)"/>
        <stop offset="0.5" stop-color="var(--holo-b)"/>
        <stop offset="1" stop-color="var(--holo-c)"/>
      </linearGradient>
    </defs>
    <circle cx="125" cy="125" r="122" fill="url(#holo-fill)"/>
  </svg>

  <span class="meta-label" style="left:92px; top:713px;">Date&nbsp;&nbsp;:</span>
  <span class="leader" style="left:178px; top:733px; width:245px;"></span>
  <span class="meta-label" style="left:92px; top:756px;">Place :</span>
  <span class="leader" style="left:183px; top:776px; width:242px;"></span>
  <span class="meta-label" style="left:891px; top:771px;">Signature</span>
</main>
</body>
</html>
```